Birthday, Anniversary, Engagement & Thank You cards

We need a foldover notecard design to send to our clients on special occasions (birthday, anniversary & engagements,) as well as a general thank you card. The design is to be the same on all cards, with the exception of the phrases "Happy Birthday," "Happy Anniversary," "Congrats on Your Engagement," and "Thank You."
Our logo needs to be on the card. Would like espresso background with orange lettering. Inside of card can be blank, as I will customize each file upon uploading to Quillmarch. Need modern, clean look with josefin font to match logo.

```html
<!DOCTYPE html>
<html lang="en">
<head>
<meta charset="utf-8">
<title>Aldermoor Foldover Notecard – Thank You</title>
<link href="https://fonts.googleapis.com/css2?family=Josefin+Sans:wght@300;400&display=swap" rel="stylesheet">
<style>
  :root {
    --espresso: #2a1911;
    --burnt-orange: #c8702c;
    --card-white: #ffffff;
    --ink: #2b2523;
    --backdrop: #e9e7ea;
    --shadow: rgba(30, 20, 30, 0.22);
  }
  * { margin: 0; padding: 0; box-sizing: border-box; }
  html, body {
    width: 1200px;
    height: 900px;
    overflow: hidden;
  }
  body {
    background: var(--backdrop);
    font-family: "Josefin Sans", sans-serif;
  }
  .notecard-set {
    position: relative;
    width: 1200px;
    height: 900px;
  }
  .card {
    position: absolute;
    top: 305px;
    width: 520px;
    height: 290px;
    box-shadow: 0 6px 18px var(--shadow);
  }
  .card--front {
    left: 50px;
    background: var(--espresso);
    display: flex;
    align-items: center;
    justify-content: center;
  }
  .card--back {
    left: 630px;
    background: var(--card-white);
  }
  .greeting {
    color: var(--burnt-orange);
    font-weight: 300;
    font-size: 58px;
    font-variant: small-caps;
    letter-spacing: 0.04em;
    line-height: 1;
    padding-top: 10px;
  }
  .studio-name {
    position: absolute;
    left: 0;
    right: 0;
    top: 212px;
    display: flex;
    align-items: center;
    justify-content: center;
    gap: 10px;
    color: var(--ink);
    font-weight: 400;
    font-size: 15px;
    letter-spacing: 0.28em;
    text-transform: uppercase;
    line-height: 1;
  }
  .studio-name__mark {
    width: 8px;
    height: 8px;
    background: var(--ink);
  }
</style>
</head>
<body>
  <main class="notecard-set">
    <section class="card card--front" aria-label="Card front">
      <h1 class="greeting">Thank You</h1>
    </section>
    <section class="card card--back" aria-label="Card back">
      <p class="studio-name"><span class="studio-name__mark" aria-hidden="true"></span>Aldermoor</p>
    </section>
  </main>
</body>
</html>
```